Florida-based Coastal Landscaping Comapny Needs Postcard Designs

We are a newly established Florida-based, coastal landscaping company that is looking for some really innovative postcards that we can use to get our name our to affluent consumers that live on the coast of Florida (think on the beach) and small to medium sized businesses in the same area. We will be sending out 100s of thousands of these, so need a great design

Target Market(s)

Affluent consumers and small to medium sized businesses

Industry/Entity Type

Landscaping

Font styles to use
Sans Serif

Colors

Designer to choose colors to be used in the design.

Requirements
Must have
• Florida - looking, island looking / paradise, but incorporate landscaping themes
• Need to say something about "Enjoy your yard this summer" or something relating to summer, landscapes and florida
• and would like to make two offers $50.00 off with signing up for one of our routine maintenance programs, or 1 free landscape inspection
Should not have
• Regular generic lawn company designs. We are a top tier landscape design / build plus maintenance firm, so not your mom and pop lawn mowing company

```html
<!DOCTYPE html>
<html lang="en">
<head>
<meta charset="utf-8">
<title>Shore Grove Summer Postcard</title>
<link href="https://fonts.googleapis.com/css2?family=Marcellus+SC&family=Oswald:wght@400;500;600&family=Jost:wght@500;600&family=Marcellus&display=swap" rel="stylesheet">
<style>
  :root {
    --page: #2b2b2b;
    --card: #ffffff;
    --brand-blue: #1f4e9c;
    --wave-blue: #1a8fd8;
    --wave-deep: #1d4fa3;
    --water-pale: rgba(236, 242, 242, 0.9);
    --ink: #26323a;
    --sage: rgba(150, 168, 132, 0.92);
    --stamp: #e7e9e9;
  }
  * { margin: 0; padding: 0; box-sizing: border-box; }
  html, body { width: 960px; height: 1200px; overflow: hidden; }
  body { background: var(--page); position: relative; }

  .postcard {
    position: absolute;
    background: var(--card);
    overflow: hidden;
  }

  /* Front */
  .postcard--front { left: 118px; top: 34px; width: 725px; height: 558px; }
  .front-photo {
    position: absolute; inset: 0;
    background: linear-gradient(180deg, #cfd6ee 0%, #7f8fd3 22%, #9fb3d8 38%, #eef1f2 55%, #d9dcd3 68%, #a6b2a6 80%, #c9d3d2 100%);
  }
  .headline {
    position: absolute; left: 0; right: 0; top: 18px;
    font-family: "Marcellus SC", "Marcellus", serif;
    color: var(--brand-blue);
    font-size: 50px; line-height: 1; letter-spacing: 1px;
    text-align: center;
  }
  .headline__accent {
    position: absolute; right: 44px; top: 70px;
    font-family: "Marcellus SC", "Marcellus", serif;
    color: #ffffff; font-size: 54px; line-height: 1; letter-spacing: 1px;
  }
  .front-wave { position: absolute; inset: 0; }
  .offer-amount {
    position: absolute; left: 30px; top: 426px;
    font-family: "Oswald", sans-serif; font-weight: 600;
    color: var(--brand-blue); font-size: 64px; line-height: 1;
  }
  .offer-off {
    position: absolute; left: 86px; top: 490px;
    font-family: "Oswald", sans-serif; font-weight: 600;
    color: var(--brand-blue); font-size: 24px; line-height: 1;
  }
  .offer-divider {
    position: absolute; left: 148px; top: 432px; height: 84px;
    border-left: 2px dotted var(--wave-blue);
  }
  .offer-detail {
    position: absolute; left: 161px; top: 454px;
    font-family: "Oswald", sans-serif; font-weight: 400;
    color: var(--brand-blue); line-height: 1.25;
  }
  .offer-detail__line1 { font-size: 19px; display: block; }
  .offer-detail__line2 { font-size: 15.5px; display: block; }
  .offer-alt {
    position: absolute; left: 30px; top: 520px;
    font-family: "Oswald", sans-serif; font-weight: 500;
    color: var(--brand-blue); font-size: 24px; line-height: 1;
  }
  .brand-name {
    font-family: "Jost", sans-serif; font-weight: 500;
    color: var(--ink); letter-spacing: 1.5px; white-space: nowrap;
  }
  .postcard--front .brand-name {
    position: absolute; left: 440px; top: 510px; font-size: 26px;
  }

  /* Back */
  .postcard--back { left: 120px; top: 616px; width: 723px; height: 557px; }
  .back-photo { position: absolute; inset: 0; }
  .contact {
    position: absolute; left: 54px; top: 392px;
    font-family: "Jost", sans-serif; color: #ffffff;
  }
  .contact__title { font-size: 40px; font-weight: 500; line-height: 1.1; letter-spacing: 0.5px; }
  .contact__phone { font-size: 42px; font-weight: 600; line-height: 1.15; letter-spacing: 1px; }
  .contact__web { font-size: 27px; font-weight: 500; line-height: 1.4; letter-spacing: 0.5px; }
  .postcard--back .brand-name {
    position: absolute; left: 384px; top: 66px; font-size: 22px;
  }
  .stamp-box {
    position: absolute; left: 594px; top: 26px; width: 103px; height: 130px;
    background: var(--stamp);
  }
</style>
</head>
<body>

<section class="postcard postcard--front">
  <div class="front-photo" role="img" aria-label="Photo of a white waterfront villa with palm trees, a boathouse and a dock over calm water"></div>

  <svg class="front-wave" width="725" height="558" viewBox="0 0 725 558" aria-hidden="true">
    <path d="M0,440 C120,362 260,345 400,410 C520,466 640,462 725,408 L725,558 L0,558 Z" fill="var(--water-pale)"/>
    <path d="M0,432 C120,350 260,330 400,398 C520,456 640,452 725,396 L725,408 C640,462 520,466 400,410 C260,345 120,362 0,440 Z" fill="var(--wave-blue)"/>
    <path d="M0,422 C120,340 260,322 400,390 C520,446 640,444 725,388 L725,396 C640,452 520,456 400,398 C260,330 120,350 0,432 Z" fill="var(--wave-deep)"/>
  </svg>

  <h1 class="headline">Enjoy your yard this</h1>
  <div class="headline__accent">Summer</div>

  <div class="offer-amount">$50</div>
  <div class="offer-off">OFF</div>
  <div class="offer-divider"></div>
  <p class="offer-detail">
    <span class="offer-detail__line1">SIGNING UP FOR ONE OF OUR</span>
    <span class="offer-detail__line2">ROUTINE MAINTENANCE PROGRAMS</span>
  </p>
  <div class="offer-alt">OR 1 FREE IRRIGATION INSPECTION</div>

  <div class="brand-name">SHORE GROVE</div>
</section>

<section class="postcard postcard--back">
  <svg class="back-photo" width="723" height="557" viewBox="0 0 723 557">
    <defs>
      <linearGradient id="backScene" x1="0" y1="0" x2="0" y2="1">
        <stop offset="0" stop-color="#2f86d6"/>
        <stop offset="0.2" stop-color="#6aa6d8"/>
        <stop offset="0.35" stop-color="#d9cf98"/>
        <stop offset="0.5" stop-color="#4f7d3b"/>
        <stop offset="0.62" stop-color="#b04f98"/>
        <stop offset="0.7" stop-color="#8f8f7c"/>
        <stop offset="0.8" stop-color="#6f8c5c"/>
        <stop offset="1" stop-color="#7c9270"/>
      </linearGradient>
    </defs>
    <path role="img" aria-label="Photo of a yellow waterfront home with tropical gardens and flowering bougainvillea above a lagoon"
          d="M0,0 L368,0 C320,90 290,200 330,290 C372,380 392,460 360,557 L0,557 Z" fill="url(#backScene)"/>
    <path d="M0,376 L380,376 C392,440 386,500 360,557 L0,557 Z" fill="var(--sage)"/>
    <path d="M368,0 C320,90 290,200 330,290 C372,380 392,460 360,557 L372,557 C404,460 384,380 342,290 C302,200 332,90 384,0 Z" fill="var(--wave-blue)"/>
    <path d="M384,0 C332,90 302,200 342,290 C384,380 404,460 372,557 L378,557 C410,460 390,380 348,290 C308,200 338,90 392,0 Z" fill="var(--wave-deep)"/>
  </svg>

  <div class="contact">
    <div class="contact__title">CONTACT US</div>
    <div class="contact__phone">123-456-789</div>
    <div class="contact__web">www.website.com</div>
  </div>

  <div class="brand-name">SHORE GROVE</div>
  <div class="stamp-box" aria-label="Stamp area"></div>
</section>

</body>
</html>
```